Design some Business Cards for Ski Trainer

1. A namecard with orange and white major color for a female Ski instructor
2. Prefer using more icons
3. Please use the same logo of http://www.frostpeakcoaching.example/ ( as seen in attached file, but you may need to reconstruct the logo again)
4. text detail for the content is attached
5. Please DO NOT use traditional fonts
6. We would like to use the font "Showcard Gothic " for the company name "Frost & Peak Coaching"

```html
<!DOCTYPE html>
<html lang="en">
<head>
<meta charset="utf-8">
<title>Frost &amp; Peak Coaching – Business Cards</title>
<link rel="stylesheet" href="https://fonts.googleapis.com/css2?family=Lilita+One&family=Open+Sans:wght@400;600&display=swap">
<style>
  :root {
    --bg: #e9e6e1;
    --card: #363636;
    --wave: #4a4a4a;
    --orange: #f2a71b;
    --orange-deep: #e08e0b;
    --white: #ffffff;
  }
  * { box-sizing: border-box; margin: 0; padding: 0; }
  html, body { width: 1200px; height: 1023px; overflow: hidden; }
  body {
    background: var(--bg);
    font-family: "Open Sans", Arial, sans-serif;
    position: relative;
  }
  .card {
    position: absolute;
    left: 180px;
    width: 840px;
    height: 470px;
    border-radius: 34px;
    background: var(--card);
    overflow: hidden;
    box-shadow: 0 10px 24px rgba(0,0,0,0.25);
  }
  .card--front { top: 26px; }
  .card--back { top: 527px; }
  .card__wave { position: absolute; inset: 0; width: 100%; height: 100%; }
  .tab {
    position: absolute;
    width: 230px;
    height: 64px;
    background: linear-gradient(180deg, var(--orange), var(--orange-deep));
  }
  .tab--top-right { top: 0; right: 60px; border-radius: 0 0 16px 16px; }
  .tab--bottom-left { bottom: 0; left: 60px; border-radius: 16px 16px 0 0; }

  .brand-mark {
    position: absolute;
    display: flex;
    align-items: center;
    gap: 12px;
    font-family: "Open Sans", Arial, sans-serif;
    font-weight: 600;
    line-height: 1;
    color: var(--white);
    letter-spacing: 2px;
  }
  .brand-mark__dot { width: 20px; height: 20px; border-radius: 50%; background: var(--orange); }

  .holder { position: absolute; right: 60px; top: 88px; text-align: right; }
  .holder__name { color: var(--white); font-size: 38px; font-weight: 400; line-height: 1.2; }
  .holder__role { color: var(--orange); font-size: 16px; font-weight: 600; line-height: 1.3; margin-top: 4px; }

  .card--front .brand-mark { right: 60px; top: 192px; font-size: 40px; }
  .divider { position: absolute; left: 440px; top: 211px; width: 190px; height: 3px; background: var(--orange); }

  .contacts { position: absolute; left: 70px; top: 250px; list-style: none; }
  .contacts li { display: flex; align-items: center; gap: 16px; color: var(--white); font-size: 19px; line-height: 1.3; margin-bottom: 12px; }
  .contacts .icon {
    width: 24px; height: 24px; border-radius: 4px;
    background: var(--orange);
    display: flex; align-items: center; justify-content: center;
    flex: none;
  }
  .contacts svg { width: 15px; height: 15px; }

  .card--back .brand-mark { left: 180px; top: 212px; font-size: 46px; }
  .company {
    position: absolute;
    right: 70px; top: 150px;
    width: 330px;
    font-family: "Lilita One", "Arial Black", sans-serif;
    font-weight: 400;
    font-size: 46px;
    line-height: 1.1;
    color: var(--orange);
    text-align: left;
  }
</style>
</head>
<body>

<section class="card card--front" aria-label="Business card front">
  <svg class="card__wave" viewBox="0 0 840 470" preserveAspectRatio="none" aria-hidden="true">
    <path d="M0 470 L0 300 C120 260 210 330 320 290 C430 250 470 120 600 110 C700 100 780 60 840 40 L840 470 Z" fill="var(--wave)" opacity="0.55"/>
  </svg>
  <div class="tab tab--top-right"></div>
  <div class="tab tab--bottom-left"></div>

  <div class="holder">
    <p class="holder__name">Mira Lindqvist</p>
    <p class="holder__role">Ski Instructor &amp; Vacation Organizer</p>
  </div>
  <div class="divider"></div>
  <div class="brand-mark"><span class="brand-mark__dot"></span>FPC</div>

  <ul class="contacts">
    <li><span class="icon"><svg viewBox="0 0 24 24"><path fill="#fff" d="M6.6 10.8a15.1 15.1 0 0 0 6.6 6.6l2.2-2.2c.3-.3.7-.4 1-.2 1.1.4 2.3.6 3.6.6.6 0 1 .4 1 1V20c0 .6-.4 1-1 1A17 17 0 0 1 3 4c0-.6.4-1 1-1h3.5c.6 0 1 .4 1 1 0 1.3.2 2.5.6 3.6.1.3 0 .7-.2 1z"/></svg></span>(852) 5550 1234</li>
    <li><span class="icon"><svg viewBox="0 0 24 24"><path fill="#fff" d="M3 5h18v14H3z"/><path fill="none" stroke="#f2a71b" stroke-width="2" d="M3 6l9 7 9-7"/></svg></span>mira.coach@example.com</li>
    <li><span class="icon"><svg viewBox="0 0 24 24"><circle cx="12" cy="12" r="8" fill="#fff"/></svg></span>Frost &amp; Peak Coaching</li>
    <li><span class="icon"><svg viewBox="0 0 24 24"><circle cx="12" cy="12" r="8" fill="none" stroke="#fff" stroke-width="2"/><path d="M4 12h16M12 4c3 3 3 13 0 16M12 4c-3 3-3 13 0 16" fill="none" stroke="#fff" stroke-width="1.6"/></svg></span>www.frostpeakcoaching.example</li>
  </ul>
</section>

<section class="card card--back" aria-label="Business card back">
  <svg class="card__wave" viewBox="0 0 840 470" preserveAspectRatio="none" aria-hidden="true">
    <path d="M0 0 L0 180 C100 160 160 90 280 70 C400 50 470 20 520 0 Z" fill="var(--wave)" opacity="0.55"/>
  </svg>
  <div class="tab tab--top-right"></div>
  <div class="tab tab--bottom-left"></div>

  <div class="brand-mark"><span class="brand-mark__dot"></span>FPC</div>
  <h1 class="company">Frost &amp; Peak Coaching</h1>
</section>

</body>
</html>
```